Vandrel Group — Business Card Design Brief
Overview
Design a double-sided business card for Vandrel Group that highlights our two service arms: Vandrel Communications (telecommunications) and Vandrel Energy (business energy solutions). The card should feel smart and stand out when handed to clients.

Objectives
Showcase our areas of specialty clearly.
Reflect the overall Vandrel / Vandrel Group brand while acknowledging both arms.
Explore using both logos (Communications + Energy) or one unified logo, depending on the design.

Deliverables
One double-sided business card design (front + back).

Content & Copy
Front (preferred): Logo: Vandrel / Vandrel Group
Descriptor: Business Communications | Business Energy
Back:My contact details and company details
Core products: Business Mobile • Telephony • Internet • Business Energy Solutions

Brand & Visual Direction
We have a group logo currently tailored more toward telecoms, plus a separate Vandrel Energy logo.
Please explore layouts that use both logos or just one, whichever works best.
Color: I wouldn't mind seeing an option using our the Blue/Purple gradient from our website (vandrel-example.co.uk), but also open to non-gradient approaches and other colours..

Overall look: Smart, modern, and distinctive.
Format & Print Specs
Double-sided business card format. (Use a standard size

Must-Haves
Front: Vandrel wording or Vandrel Group wording with atleast 1 logo also on front “Business Communications | Business Energy.”

Back: Contact + company details and core products.
A design that stands out while remaining professional.

Nice-to-Have Options
A gradient version using our site’s Blue/Purple gradient.
A non-gradient version.
A dual-logo treatment versus a single-logo treatment.

Thanks
Dominic

```html
<!DOCTYPE html>
<html lang="en">
<head>
<meta charset="utf-8">
<title>Vandrel Group — Business Card</title>
<link rel="stylesheet" href="https://fonts.googleapis.com/css2?family=Montserrat:wght@400;500;700;800&display=swap">
<style>
  :root {
    --stage: #2b2b2d;
    --navy: #27205f;
    --ink: #231c5c;
    --white: #ffffff;
    --lime: #c9d21a;
    --green: #4caf3c;
    --blue: #2a6fc9;
    --sky: #29a3dc;
    --text-grey: #1f1f2a;
  }
  * { box-sizing: border-box; margin: 0; padding: 0; }
  html, body {
    width: 1200px; height: 875px; overflow: hidden;
    background: var(--stage);
    font-family: "Montserrat", sans-serif;
  }
  .canvas { position: relative; width: 1200px; height: 875px; }

  .card {
    position: absolute;
    width: 540px; height: 310px;
    border-radius: 18px;
    overflow: hidden;
  }

  /* Front */
  .card--front { left: 40px; top: 170px; background: var(--navy); color: var(--white); }
  .front-brand {
    position: absolute; left: 0; right: 0; top: 100px;
    display: flex; align-items: center; justify-content: center; gap: 18px;
  }
  .brand-dot { width: 56px; height: 56px; border-radius: 50%; flex: none; }
  .card--front .brand-dot { background: var(--green); }
  .front-brand .brand-name {
    font-weight: 800; font-size: 62px; letter-spacing: 1px; line-height: 1;
    color: var(--white);
  }
  .descriptor {
    position: absolute; left: 0; right: 0; bottom: 36px;
    display: flex; justify-content: center; align-items: center; gap: 14px;
    font-size: 14px; font-weight: 500; letter-spacing: 0.5px;
  }
  .descriptor .divider { width: 2px; height: 16px; background: var(--lime); }

  /* Back */
  .card--back { left: 620px; top: 395px; background: var(--white); color: var(--text-grey); }
  .back-brand {
    position: absolute; left: 34px; top: 28px;
    font-weight: 800; font-size: 52px; line-height: 1; color: var(--ink); letter-spacing: 1px;
  }
  .card--back .brand-dot {
    position: absolute; right: 48px; top: 34px; width: 90px; height: 90px;
    background: var(--blue);
  }
  .person { position: absolute; left: 34px; top: 100px; }
  .person-name { font-weight: 800; font-size: 21px; color: var(--ink); line-height: 1.2; }
  .person-role { font-size: 12.5px; font-weight: 500; margin-top: 2px; }
  .address { position: absolute; left: 34px; top: 154px; font-size: 12px; line-height: 1.35; font-style: normal; }
  .contact-list { position: absolute; left: 34px; top: 192px; list-style: none; font-size: 12px; }
  .contact-list li { display: flex; align-items: center; gap: 8px; line-height: 1.6; }
  .contact-list svg { width: 12px; height: 12px; fill: var(--sky); flex: none; }

  .product-list {
    position: absolute; left: 34px; right: 34px; bottom: 16px;
    display: flex; gap: 12px;
    list-style: none; font-size: 11.5px; font-weight: 500; color: var(--ink);
  }
  .product-list li { display: flex; align-items: center; gap: 6px; white-space: nowrap; }
  .product-list li::before {
    content: ""; width: 6px; height: 6px; border-radius: 50%; background: var(--sky);
  }
</style>
</head>
<body>
<main class="canvas">

  <section class="card card--front" aria-label="Card front">
    <div class="front-brand">
      <span class="brand-dot"></span>
      <span class="brand-name">VANDREL</span>
    </div>
    <p class="descriptor">
      <span>Business Communications</span>
      <span class="divider" aria-hidden="true"></span>
      <span>Business Energy</span>
    </p>
  </section>

  <section class="card card--back" aria-label="Card back">
    <div class="back-brand">VANDREL</div>
    <span class="brand-dot"></span>
    <div class="person">
      <p class="person-name">Dominic Ashcombe</p>
      <p class="person-role">Business Development Manager</p>
    </div>
    <address class="address">48 Kestrel Court,<br>Leeds, UK</address>
    <ul class="contact-list">
      <li>
        <svg viewBox="0 0 24 24" aria-hidden="true"><path d="M6.6 10.8a15 15 0 0 0 6.6 6.6l2.2-2.2c.3-.3.7-.4 1-.2 1.1.4 2.3.6 3.6.6.6 0 1 .4 1 1V20c0 .6-.4 1-1 1C10.6 21 3 13.4 3 4c0-.6.4-1 1-1h3.5c.6 0 1 .4 1 1 0 1.3.2 2.5.6 3.6.1.3 0 .7-.2 1z"/></svg>
        +44 (0)1632 960 418
      </li>
      <li>
        <svg viewBox="0 0 24 24" aria-hidden="true"><path d="M2 5h20v14H2zm2 2v.5l8 5 8-5V7l-8 5z"/></svg>
        dominic.ashcombe@vandrel-example.co.uk
      </li>
      <li>
        <svg viewBox="0 0 24 24" aria-hidden="true"><circle cx="12" cy="12" r="10"/></svg>
        www.vandrel-example.co.uk
      </li>
    </ul>
    <ul class="product-list">
      <li>Business Mobile</li>
      <li>Telephony</li>
      <li>Internet</li>
      <li>Business Energy Solutions</li>
    </ul>
  </section>

</main>
</body>
</html>
```